Metal head/ Sushi chef wanting artistic yet high imact business card

I'm sushi chef for make living in Australia originally from Tokyo Japan.
I'm also guitarist/composer as well on progressive metalcore/djent genre.
My favorite visual art is Mandala. Sacred geometries, Fractals, Paisleys are also things fit in me. I like dark color, earth color, and sometimes psychedelic patterns.
I want to hand out my business card when I meet new people in music industries or someone who is wanting private sushi chef for their party.
I know metal and sushi are far different subjects but they are all my passion. I would like to work with the designer who can create something cool from information above.

https://www.vidlorix.com/channel/QX8p4LtRwe7JnVb2kHs9DY3m
https://tunebarrel.com/user-804716273

Front
my name, Haruki Motobe
occupation, "Sushi chef" "Metal guitarist/composer"
Email address, pelvonmist@tavemail.net
Phone number, (61)498201753

Back:
My Vidlorix channel, Friendquay, Tunebarrel, Pictavio. All of those are searchable by "Pelvonmist" The website mentioned above can be described as their logos.

Target Market(s)

people in Music industry, such as musicians, venue managers, promoters.
People who wants to have private sushi chef for their private function, party or events.

Industry/Entity Type

Artists

Contact Information for Business Card

Uploaded photos are just image reference. not thinking to use them.
My details:
I like :
energetic music that has a lot of details such as Progressive metalcore, jazz, djent, psychedelic music.
Spiritual thoughs, Buddism, fundamentals, relaxation music, 420, weed culture, Free thoughts
U.S street culture, skate board, brelks, surf, bicycle, nature, camping, hiking, ocean, mountain, desert, countryside,
permaculture, natural farming, organic farming, compost, self sufficient.
nigiri sushi, art sushi, something/someone beautiful in mind.

Dislike:
Fakes, Bullshits, format, negative, preservatives, artificial colors, illuminati, satanism, manipulation, mass favorites, big society, politics, Chinese letters on western design

Colors
0455a3
000000
7c7c7c
00a990
acd036
f37122

Requirements
Must have
• Front
• my name, Haruki Motobe
• occupation, "Sushi chef" "Metal guitarist/composer"
• Email address, pelvonmist@tavemail.net
• Phone number, (61)498201753
• Back:
• My Vidlorix channel, Friendquay, Tunebarrel, Pictavio. All of those are searchable by "Pelvonmist" The website mentioned above can be described as their logos.
Nice to have
• something based on one of those either back ground or logo:
• Mandala, Sacred Geometry, Fractal art
Should not have
• pop essence. mass favorites, pink, Chinese letters, asian fonts, something asian

```html
<!DOCTYPE html>
<html lang="en">
<head>
<meta charset="utf-8">
<title>Haruki Motobe – Business Card</title>
<link rel="stylesheet" href="https://fonts.googleapis.com/css2?family=Lato:wght@400;700;900&display=swap">
<style>
  :root {
    --stage: #d9d9d9;
    --card-light: #fcf8f7;
    --card-dark: #1b1b1b;
    --ink: #111111;
    --paper-text: #f2f2f2;
    --rule-red: #b8322e;
    --rule-orange: #e0894a;
    --tunebarrel: #f37122;
    --vidlorix: #d62a1e;
    --photo-a: #f6a33a;
    --photo-b: #c3301a;
    --photo-c: #1a0b08;
  }
  * { box-sizing: border-box; margin: 0; padding: 0; }
  html, body { width: 1200px; height: 782px; overflow: hidden; }
  body {
    background: var(--stage);
    font-family: "Lato", Arial, sans-serif;
    color: var(--ink);
    position: relative;
  }
  .card {
    position: absolute;
    left: 300px;
    width: 600px;
    height: 343px;
    box-shadow: 0 4px 14px rgba(0,0,0,0.25);
  }
  /* Back */
  .card--back {
    top: 22px;
    background: var(--card-dark);
    color: var(--paper-text);
  }
  .back-links {
    position: absolute;
    left: 0; right: 0; top: 205px;
    text-align: center;
  }
  .platforms {
    display: flex;
    justify-content: center;
    gap: 18px;
    margin-bottom: 10px;
    font-size: 11px;
    font-weight: 700;
  }
  .platform { display: flex; align-items: center; gap: 5px; }
  .platform__mark { width: 14px; height: 14px; border-radius: 3px; }
  .platform--tunebarrel .platform__mark { background: var(--tunebarrel); }
  .platform--vidlorix .platform__mark { background: var(--vidlorix); }
  .url { font-size: 14px; line-height: 1.35; letter-spacing: 0.2px; }

  /* Front */
  .card--front {
    top: 417px;
    background: var(--card-light);
  }
  .portrait {
    position: absolute;
    left: 100px; top: 42px;
    width: 226px; height: 160px;
    background: radial-gradient(circle at 30% 25%, var(--photo-a), var(--photo-b) 45%, var(--photo-c) 100%);
  }
  .identity {
    position: absolute;
    left: 342px; top: 112px;
  }
  .identity__name {
    font-size: 19px; font-weight: 900; letter-spacing: 0.5px;
    text-transform: uppercase;
  }
  .identity__role { font-size: 14px; margin-top: 2px; }
  .contact { margin-top: 10px; font-size: 15px; line-height: 1.35; }
  .contact__row { display: flex; align-items: center; gap: 5px; }
  .contact__row svg { width: 13px; height: 13px; }

  .social-rule {
    position: absolute;
    left: 0; right: 0; top: 214px;
    display: flex; align-items: center;
  }
  .rule-short { width: 38px; height: 3px; background: var(--rule-red); margin-left: 20px; }
  .social {
    display: flex; align-items: center; gap: 5px;
    margin-left: 8px; font-size: 15px; font-weight: 400;
  }
  .social__dot { width: 16px; height: 16px; border-radius: 50%; background: var(--ink); }
  .rule-long {
    flex: 1; height: 3px; margin-left: 8px;
    background: linear-gradient(90deg, var(--rule-red), var(--rule-orange));
  }
</style>
</head>
<body>

<section class="card card--back" aria-label="Card back">
  <div class="back-links">
    <div class="platforms">
      <span class="platform platform--tunebarrel"><span class="platform__mark"></span>Tunebarrel</span>
      <span class="platform platform--vidlorix"><span class="platform__mark"></span>Vidlorix</span>
    </div>
    <p class="url">www.tunebarrel.com/user-804716273</p>
    <p class="url">www.vidlorix.com/channel/QX8p4LtRwe7JnVb2kHs9DY3m</p>
  </div>
</section>

<section class="card card--front" aria-label="Card front">
  <div class="portrait" role="img" aria-label="Portrait of the guitarist in front of a fiery red sun"></div>

  <div class="identity">
    <h1 class="identity__name">Haruki Motobe</h1>
    <p class="identity__role">Sushi chef, Metal guitarist/composer</p>
    <div class="contact">
      <p class="contact__row">
        <svg viewBox="0 0 16 16" aria-hidden="true"><path d="M2 6c0-2 2-3 6-3s6 1 6 3v1h-3V5.5H5V7H2z M4 8h8l2 5H2z" fill="#111"/></svg>
        (61)498201753
      </p>
      <p class="contact__row">
        <svg viewBox="0 0 16 16" aria-hidden="true"><rect x="1" y="3" width="14" height="10" fill="#111"/><path d="M1.5 3.5 8 9l6.5-5.5" stroke="#fcf8f7" stroke-width="1.3" fill="none"/></svg>
        pelvonmist@tavemail.net
      </p>
    </div>
  </div>

  <div class="social-rule">
    <span class="rule-short"></span>
    <span class="social">
      <span class="social__dot" aria-hidden="true"></span>
      <span class="social__dot" aria-hidden="true"></span>
      Pelvonmist
    </span>
    <span class="rule-long"></span>
  </div>
</section>

</body>
</html>
```